Real Estate Webpage Design

We have an existing website: brindlewoodhomes.com.au
We focus customised service mainly on Property Management and second-hand property sales.
We are not entirely happy about the current design and layout can stay roughly the same as the back end coding is linked to a CRM system.
We would like to see the design are more reachable to our clients and appearing.
Please check our Website Design Draft for more details.

Industry/Entity Type

Real estate Agency

Number of Pages Required

5+ page

Font styles to use
Sans Serif

Colors

Designer to choose colors to be used in the design.

```html
<!DOCTYPE html>
<html lang="en">
<head>
<meta charset="utf-8">
<title>Brindlewood Property Group</title>
<link href="https://fonts.googleapis.com/css2?family=Open+Sans:wght@300;400;600&family=Raleway:wght@200;300&display=swap" rel="stylesheet">
<style>
:root{
  --orange:#f4ae2a;
  --header-bg:#efefef;
  --text:#626262;
  --text-dark:#4f4f4f;
  --line:#e3e3e3;
  --band:#f4f4f4;
  --navy:#2c3340;
  --overlay:rgba(38,46,78,.88);
  --white:#ffffff;
}
*{margin:0;padding:0;box-sizing:border-box}
html,body{width:794px;height:1200px;overflow:hidden;background:var(--white)}
body{position:relative;font-family:"Open Sans",Arial,sans-serif;color:var(--text)}
.abs{position:absolute}

/* header */
.site-header{position:absolute;left:0;top:0;width:794px;height:69px;background:var(--header-bg)}
.brand{position:absolute;left:79px;top:21px;display:flex;align-items:center;gap:6px}
.brand-mark{width:20px;height:20px;background:var(--orange)}
.brand-name{font-family:"Open Sans",Arial,sans-serif;font-weight:600;font-size:17px;color:var(--orange);line-height:1}
.brand-sub{position:absolute;left:119px;top:47px;font-size:5.5px;color:#555}
.main-nav a{position:absolute;top:28px;font-size:8.6px;color:#666;text-decoration:none;white-space:nowrap}
.main-nav a.active{color:var(--orange)}
.main-nav a.active::after{content:"";position:absolute;left:-5px;right:0;bottom:-2px;height:1px;background:#777}

/* hero */
.hero{position:absolute;left:0;top:69px;width:794px;height:345px;
  background:radial-gradient(ellipse at 62% 55%,rgba(150,120,80,.55) 0%,rgba(40,40,70,0) 40%),
  linear-gradient(180deg,#1a1f52 0%,#1e2a6a 45%,#13183a 75%,#05060e 100%)}
.hero-title{position:absolute;left:0;width:794px;top:119px;text-align:center;font-family:"Raleway",Arial,sans-serif;font-weight:300;font-size:24px;color:var(--white);letter-spacing:.3px}
.hero-btn{position:absolute;left:321px;top:187px;width:153px;height:25px;border-radius:13px;background:var(--orange);color:var(--white);font-size:8.4px;font-weight:600;display:flex;align-items:center;justify-content:center;gap:6px}

/* intro */
.intro-title{position:absolute;left:0;width:794px;top:438px;text-align:center;font-weight:300;font-size:19px;color:var(--orange);letter-spacing:.5px}
.intro-text{position:absolute;left:80px;width:634px;text-align:center;font-size:13px;line-height:17px;color:var(--text);letter-spacing:.5px}
.divider{position:absolute;left:79px;top:639px;width:636px;height:1px;background:var(--line)}

/* listings */
.listings-title{position:absolute;left:0;width:794px;top:660px;text-align:center;font-weight:300;font-size:14.5px;color:var(--text-dark);letter-spacing:.6px}
.tab{position:absolute;top:696px;font-weight:300;font-size:14px;color:#777}
.tab.active{color:var(--orange)}
.card{position:absolute;top:733px;width:139px;height:170px;background:#f7f7f7}
.card-photo{width:139px;height:126px}
.card-info{position:relative;height:44px;font-size:6.3px;color:#444}
.card-suburb{position:absolute;left:3px;top:5px}
.card-price{position:absolute;right:3px;top:5px}
.card-address{position:absolute;left:3px;top:15px}
.card-icons{position:absolute;left:5px;right:3px;top:27px;height:10px}
.card-icons svg{position:absolute;top:0}
.card-icons span{position:absolute;top:3px;font-size:5px}
.card-overlay{position:absolute;left:0;top:0;width:139px;height:170px;background:var(--overlay);color:var(--white);font-size:6.3px}
.slider-arrow{position:absolute;top:793px}
.view-all{position:absolute;left:652px;top:917px;font-size:6.5px;color:var(--orange);text-decoration:underline}

/* testimonials */
.testimonials{position:absolute;left:0;top:945px;width:794px;height:134px;background:var(--band);border-top:1px solid #e8e8e8;border-bottom:1px solid #e8e8e8}
.testimonials h2{position:absolute;left:0;width:794px;top:33px;text-align:center;font-weight:400;font-size:15.5px;color:var(--orange);letter-spacing:1.2px}
.testimonials p{position:absolute;left:0;width:794px;top:75px;text-align:center;font-size:10.6px;line-height:13px;color:#666;letter-spacing:.3px}

/* social */
.social{position:absolute;top:1102px;width:37px;height:37px;border:1px solid #333;display:flex;align-items:center;justify-content:center}
.social.active{background:var(--navy)}
.social i{display:block;width:6px;height:6px;border-radius:50%;background:#333}
.social.active i{background:var(--white)}

/* footer */
.site-footer{position:absolute;left:0;top:1158px;width:794px;height:42px;background:var(--navy)}
.site-footer a{position:absolute;top:12px;font-size:13px;color:#e6e6e6;text-decoration:none;white-space:nowrap}
</style>
</head>
<body>

<header class="site-header">
  <div class="brand"><span class="brand-mark"></span><span class="brand-name">Brindlewood</span></div>
  <div class="brand-sub">Property Group</div>
  <nav class="main-nav">
    <a class="active" href="#" style="left:331px">Home</a>
    <a href="#" style="left:377px">About Us</a>
    <a href="#" style="left:438px">Leasing</a>
    <a href="#" style="left:492px">Buy</a>
    <a href="#" style="left:529px">Sell</a>
    <a href="#" style="left:565px">Our Team</a>
    <a href="#" style="left:629px">Blog</a>
    <a href="#" style="left:669px">Contact Us</a>
  </nav>
</header>

<section class="hero" role="img" aria-label="Night view of a lit waterfront house with a timber pergola beside a marina">
  <h1 class="hero-title">Chosen for our service. Famous for our results.</h1>
  <div class="hero-btn">START HERE <svg width="10" height="5" viewBox="0 0 10 5"><path d="M0 2.5H9M7 .5L9 2.5 7 4.5" stroke="#fff" stroke-width=".8" fill="none"/></svg></div>
</section>

<h2 class="intro-title">Brindlewood – built around “the home”</h2>
<p class="intro-text" style="top:482px">Brindlewood stands for “the home, the house”, buying a property is one of the most expensive expenses and important assets for people. Brindlewood is a real estate company located in Gungahlin, Canberra.</p>
<p class="intro-text" style="top:550px">Being a portfolio sales agent and property manager, coupled with our high-profile international real estate experience, Brindlewood is considered a market leader on the cutting edge with deep industry knowledge, ranging from landlord-tenant relationships, residential purchases.</p>
<div class="divider"></div>

<h2 class="listings-title">NEW PROPERTIES AT BRINDLEWOOD PROPERTY GROUP</h2>
<span class="tab" style="left:185px">For Sale</span>
<span class="tab active" style="left:273px">For Lease</span>
<span class="tab" style="left:374px">Open Times</span>
<span class="tab" style="left:490px">Sold</span>
<span class="tab" style="left:553px">Leased</span>

<svg class="slider-arrow" style="left:79px" width="22" height="53" viewBox="0 0 22 53"><path d="M21 1L1 26.5 21 52" stroke="#f4ae2a" fill="none"/></svg>
<svg class="slider-arrow" style="left:693px" width="22" height="53" viewBox="0 0 22 53"><path d="M1 1L21 26.5 1 52" stroke="#f4ae2a" fill="none"/></svg>

<article class="card" style="left:107px">
  <div class="card-photo" role="img" aria-label="Empty open-plan living room with timber floor and staircase" style="background:linear-gradient(160deg,#e6e4e0 0%,#c9c6c1 55%,#7a6a5c 100%)"></div>
  <div class="card-info">
    <span class="card-suburb">LAWSON</span><span class="card-price">$640 - $660 PW</span>
    <span class="card-address">27/56 WATTLEBROOK TERRACE LAWSON</span>
    <div class="card-icons">
      <svg style="left:0" width="8" height="7"><rect x=".5" y="2" width="7" height="4" fill="none" stroke="#555" stroke-width=".7"/></svg><span style="left:10px">3</span>
      <svg style="left:24px" width="8" height="7"><path d="M.5 1V6H7.5V3.5H1" fill="none" stroke="#555" stroke-width=".7"/></svg><span style="left:34px">2</span>
      <svg style="left:47px" width="8" height="7"><rect x=".5" y=".5" width="7" height="6" fill="none" stroke="#555" stroke-width=".7"/></svg><span style="left:57px">2</span>
      <svg style="left:95px" width="9" height="9"><circle cx="4.5" cy="4.5" r="3.8" fill="none" stroke="#555" stroke-width=".7"/><path d="M4.5 2V4.5H6.5" stroke="#555" stroke-width=".7" fill="none"/></svg>
      <svg style="left:108px" width="10" height="8"><rect x=".5" y="1" width="9" height="6" fill="none" stroke="#555" stroke-width=".7"/><path d="M.5 1L5 4.5 9.5 1" stroke="#555" stroke-width=".7" fill="none"/></svg>
      <svg style="left:122px" width="10" height="10"><path d="M5 .5L6.3 3.6 9.5 3.8 7 5.9 7.8 9.2 5 7.4 2.2 9.2 3 5.9 .5 3.8 3.7 3.6Z" fill="none" stroke="#555" stroke-width=".7"/></svg>
    </div>
  </div>
</article>

<article class="card" style="left:254px">
  <div class="card-photo" role="img" aria-label="Balcony with glass balustrade under a blue cloudy sky" style="background:linear-gradient(180deg,#3f78c9 0%,#9fbde3 40%,#d2d3d3 70%,#bdbcbb 100%)"></div>
  <div class="card-info">
    <span class="card-suburb">RED HILL</span><span class="card-price">$1400 PW</span>
    <span class="card-address">9 KESTREL STREET RED HILL</span>
    <div class="card-icons">
      <svg style="left:0" width="8" height="7"><rect x=".5" y="2" width="7" height="4" fill="none" stroke="#555" stroke-width=".7"/></svg><span style="left:10px">4</span>
      <svg style="left:24px" width="8" height="7"><path d="M.5 1V6H7.5V3.5H1" fill="none" stroke="#555" stroke-width=".7"/></svg><span style="left:34px">2</span>
      <svg style="left:47px" width="8" height="7"><rect x=".5" y=".5" width="7" height="6" fill="none" stroke="#555" stroke-width=".7"/></svg><span style="left:57px">2</span>
      <svg style="left:108px" width="10" height="8"><rect x=".5" y="1" width="9" height="6" fill="none" stroke="#555" stroke-width=".7"/><path d="M.5 1L5 4.5 9.5 1" stroke="#555" stroke-width=".7" fill="none"/></svg>
      <svg style="left:122px" width="10" height="10"><path d="M5 .5L6.3 3.6 9.5 3.8 7 5.9 7.8 9.2 5 7.4 2.2 9.2 3 5.9 .5 3.8 3.7 3.6Z" fill="none" stroke="#555" stroke-width=".7"/></svg>
    </div>
  </div>
</article>

<article class="card" style="left:402px">
  <div class="card-photo" role="img" aria-label="Single-storey brick house at dusk" style="height:170px;background:linear-gradient(180deg,#4a5878 0%,#3d4764 60%,#2e3550 100%)"></div>
  <div class="card-overlay">
    <span class="abs" style="left:0;width:139px;text-align:center;top:134px">BRADDON</span>
    <span class="abs" style="left:0;width:139px;text-align:center;top:145px">215/2 MARLOWE STREET BRADDON</span>
    <span class="abs" style="left:12px;top:156px">$560 PW</span>
    <span class="abs" style="left:93px;top:156px">MORE <svg width="10" height="5" viewBox="0 0 10 5"><path d="M0 2.5H9M7 .5L9 2.5 7 4.5" stroke="#fff" stroke-width=".7" fill="none"/></svg></span>
  </div>
</article>

<article class="card" style="left:549px">
  <div class="card-photo" role="img" aria-label="Modern kitchen and dining area with white chairs" style="background:linear-gradient(180deg,#3b3040 0%,#4a4450 50%,#c9c9cf 100%)"></div>
  <div class="card-info">
    <span class="card-suburb">BRADDON</span><span class="card-price">$560 PW</span>
    <span class="card-address">215/2 MARLOWE STREET BRADDON</span>
    <div class="card-icons">
      <svg style="left:0" width="8" height="7"><rect x=".5" y="2" width="7" height="4" fill="none" stroke="#555" stroke-width=".7"/></svg><span style="left:10px">1</span>
      <svg style="left:24px" width="8" height="7"><path d="M.5 1V6H7.5V3.5H1" fill="none" stroke="#555" stroke-width=".7"/></svg><span style="left:34px">1</span>
      <svg style="left:47px" width="8" height="7"><rect x=".5" y=".5" width="7" height="6" fill="none" stroke="#555" stroke-width=".7"/></svg><span style="left:57px">1</span>
      <svg style="left:108px" width="10" height="8"><rect x=".5" y="1" width="9" height="6" fill="none" stroke="#555" stroke-width=".7"/><path d="M.5 1L5 4.5 9.5 1" stroke="#555" stroke-width=".7" fill="none"/></svg>
      <svg style="left:122px" width="10" height="10"><path d="M5 .5L6.3 3.6 9.5 3.8 7 5.9 7.8 9.2 5 7.4 2.2 9.2 3 5.9 .5 3.8 3.7 3.6Z" fill="none" stroke="#555" stroke-width=".7"/></svg>
    </div>
  </div>
</article>

<a class="view-all" href="#">VIEW ALL</a>

<section class="testimonials">
  <h2>TESTIMONIALS</h2>
  <svg class="abs" style="left:127px;top:82px" width="11" height="23" viewBox="0 0 11 23"><path d="M10 1L1 11.5 10 22" stroke="#f4ae2a" fill="none"/></svg>
  <p>We loved working with Brindlewood Property Group.<br>Very professional. Quick to attend to queries and concerns. High recommended.</p>
  <svg class="abs" style="left:656px;top:82px" width="11" height="23" viewBox="0 0 11 23"><path d="M1 1L10 11.5 1 22" stroke="#f4ae2a" fill="none"/></svg>
</section>

<a class="social" href="#" style="left:278px" aria-label="Social profile one"><i></i></a>
<a class="social active" href="#" style="left:347px" aria-label="Social profile two"><i></i></a>
<a class="social" href="#" style="left:416px" aria-label="Social profile three"><i></i></a>
<a class="social" href="#" style="left:479px" aria-label="Social profile four"><i></i></a>

<footer class="site-footer">
  <a href="#" style="left:81px">Privacy</a>
  <a href="#" style="left:149px">Complaint Handling &amp; Dispute Resolution</a>
  <a href="#" style="left:414px">Due Diligence Checklist</a>
  <a href="#" style="left:574px">Sitemap</a>
  <a href="#" style="left:648px">Contact Us</a>
</footer>

</body>
</html>
```